Bref créative
Business Cards & Satationary for Copperfield Homes
Dallin Marsh
Professional
Copperfield Homes
PO Box 587
KELMORE RISE Q 4390
M: 0417 562 908
info@copperfieldhomes.com.au
www.copperfieldhomes.com.au
NHRA Licence No. 80394. Housing Registry Office of Tasmania No. HR-K61402
Residential Construction
"Builder of Quality not Quantity"
E:info@copperfieldhomes.com.au

```html
<!DOCTYPE html>
<html lang="en">
<head>
<meta charset="utf-8">
<title>Copperfield Homes Stationery</title>
<link href="https://fonts.googleapis.com/css2?family=Open+Sans:wght@400;600;700&display=swap" rel="stylesheet">
<style>
:root{
  --bg:#ece7e1;
  --paper:#ffffff;
  --brand:#d24a2c;
  --brand-dark:#b13a20;
  --brand-faint:#f6ded8;
  --grey:#6f6f70;
  --grey-light:#c9c9c9;
  --ink:#5a5a5a;
  --label:#8b7a6a;
}
*{box-sizing:border-box;margin:0;padding:0}
html,body{width:1200px;height:446px;overflow:hidden}
body{background:var(--bg);font-family:"Open Sans",Arial,sans-serif;color:var(--ink);position:relative}
.sheet{position:absolute;background:var(--paper);box-shadow:0 2px 6px rgba(0,0,0,.18)}
.label{position:absolute;font-size:5px;letter-spacing:.6px;text-transform:uppercase;color:var(--label);text-align:center}
.brand{display:flex;align-items:center;gap:3px}
.brand-mark{background:var(--brand)}
.brand-name{color:var(--brand);font-weight:700;text-transform:uppercase;letter-spacing:.3px;line-height:1}
.tagline{color:var(--grey);text-transform:uppercase;letter-spacing:.8px}
.contact{color:var(--ink);line-height:1.45}
.faint-square{position:absolute;background:var(--brand-faint)}
.band{position:absolute;left:0;right:0}
.band-red{background:var(--brand)}
.band-grey{background:var(--grey-light)}
.footer-note{position:absolute;left:0;right:0;text-align:center;font-size:3.6px;color:var(--grey)}

/* business cards */
.card-front{left:10px;top:114px;width:48px;height:30px;padding:4px}
.card-front .brand-mark{width:4px;height:4px}
.card-front .brand-name{font-size:3.4px}
.card-front .contact{font-size:1.9px;margin-top:3px}
.card-front .band{bottom:0;height:2px}
.card-back{left:10px;top:168px;width:48px;height:30px;background:var(--brand);display:flex;align-items:center;justify-content:center}
.card-back .brand-name{color:#fff;font-size:3.6px}

/* letterheads */
.letterhead{top:12px;width:270px;height:405px}
.letterhead-one{left:114px}
.letterhead-two{left:408px}
.letterhead .brand{position:absolute;top:20px}
.letterhead .brand-mark{width:12px;height:12px}
.letterhead .brand-name{font-size:9px}
.letterhead .tagline{position:absolute;top:34px;font-size:3.6px}
.letterhead-one .brand{left:24px}
.letterhead-one .tagline{left:39px}
.letterhead-two .brand{left:0;right:0;justify-content:center}
.letterhead-two .tagline{left:0;right:0;text-align:center}
.letterhead .contact{position:absolute;top:20px;left:150px;font-size:3.8px}
.letterhead-one .faint-square{right:0;bottom:24px;width:112px;height:112px}
.letterhead-two .faint-square{left:70px;bottom:60px;width:130px;height:120px}
.letterhead .band-red{bottom:10px;height:4px}
.letterhead .band-grey{bottom:5px;height:3px}
.letterhead .footer-note{bottom:20px}

/* envelopes */
.envelope{left:842px;width:352px;height:88px;overflow:hidden}
.envelope svg{position:absolute;left:0;top:0}
.envelope .brand{position:absolute;left:0;right:0;top:50px;justify-content:center}
.envelope .brand-mark{width:12px;height:12px}
.envelope .brand-name{font-size:8px}
.envelope-red{top:12px;background:var(--brand)}
.envelope-grey{top:100px;background:#dadada}
.envelope-white{top:188px;background:var(--paper)}
.envelope-red .brand-name{color:#fff}
.envelope-red .brand-mark{background:#fff}

/* compliment slip */
.slip{left:792px;top:312px;width:256px;height:100px;padding:14px 18px}
.slip .brand-mark{width:9px;height:9px}
.slip .brand-name{font-size:7px}
.slip .motto{font-size:4px;color:var(--grey);margin-top:6px}
.slip .band-red{bottom:6px;height:3px}
.slip .band-grey{bottom:2px;height:2px}
</style>
</head>
<body>

<div class="label" style="left:4px;top:98px;width:60px;text-align:left">Stationery Concepts</div>

<section class="sheet card-front">
  <div class="brand"><span class="brand-mark"></span><span class="brand-name">Copperfield Homes</span></div>
  <p class="contact">Dallin Marsh<br>M: 0417 562 908<br>E:info@copperfieldhomes.com.au</p>
  <div class="band band-red"></div>
</section>
<div class="label" style="left:6px;top:150px;width:56px">Business Card Front</div>

<section class="sheet card-back">
  <span class="brand-name">Copperfield Homes</span>
</section>
<div class="label" style="left:6px;top:204px;width:56px">Business Card Back</div>

<section class="sheet letterhead letterhead-one">
  <div class="brand"><span class="brand-mark"></span><span class="brand-name">Copperfield Homes</span></div>
  <div class="tagline">Residential Construction</div>
  <p class="contact">PO Box 587<br>KELMORE RISE Q 4390<br>M: 0417 562 908<br>info@copperfieldhomes.com.au<br>www.copperfieldhomes.com.au</p>
  <div class="faint-square"></div>
  <p class="footer-note">NHRA Licence No. 80394. Housing Registry Office of Tasmania No. HR-K61402</p>
  <div class="band band-red"></div>
  <div class="band band-grey"></div>
</section>
<div class="label" style="left:114px;top:424px;width:270px">Letterhead Option 1</div>

<section class="sheet letterhead letterhead-two">
  <div class="brand"><span class="brand-mark"></span><span class="brand-name">Copperfield Homes</span></div>
  <div class="tagline">Residential Construction</div>
  <div class="faint-square"></div>
  <p class="footer-note">PO Box 587 · KELMORE RISE Q 4390 · M: 0417 562 908 · www.copperfieldhomes.com.au</p>
  <div class="band band-red"></div>
  <div class="band band-grey"></div>
</section>
<div class="label" style="left:408px;top:424px;width:270px">Letterhead Option 2</div>

<section class="sheet envelope envelope-red">
  <svg width="352" height="88"><polygon points="0,0 352,0 176,44" fill="var(--brand-dark)"/></svg>
  <div class="brand"><span class="brand-mark"></span><span class="brand-name">Copperfield Homes</span></div>
</section>
<section class="sheet envelope envelope-grey">
  <svg width="352" height="88"><polygon points="0,0 352,0 176,44" fill="var(--grey)"/></svg>
  <div class="brand"><span class="brand-mark"></span><span class="brand-name">Copperfield Homes</span></div>
</section>
<section class="sheet envelope envelope-white">
  <svg width="352" height="88"><polygon points="0,0 352,0 176,44" fill="#efefef"/></svg>
  <div class="brand"><span class="brand-mark"></span><span class="brand-name">Copperfield Homes</span></div>
</section>

<section class="sheet slip">
  <div class="brand"><span class="brand-mark"></span><span class="brand-name">Copperfield Homes</span></div>
  <p class="motto">"Builder of Quality not Quantity"</p>
  <div class="band band-red"></div>
  <div class="band band-grey"></div>
</section>
<div class="label" style="left:1050px;top:424px;width:140px">Envelope Option 3</div>

</body>
</html>
```